KGDB Business Card

Looking for a business card design to incorporate our branding. We want to only use the colors listing in the Branding Package (attached).
Updates

Target Market(s)

People who need their phone or device fixed.

Industry/Entity Type

Electronics

Contact Information for Business Card

Please use:

Bright Circuit Mending Depot LLC
3478 S Ridge Trail 2210 E
Suite 417
San Antonio, TX 78341

Marcus Delwyn, Store Manager

(210) 555-0143

Requirements
Must have
• Must include the colors that are contained within the Branding Package PDF file.

```html
<!DOCTYPE html>
<html lang="en">
<head>
<meta charset="utf-8">
<title>KGDB Business Card</title>
<link rel="stylesheet" href="https://fonts.googleapis.com/css2?family=Alegreya+Sans:ital,wght@0,400;0,700;1,400&display=swap">
<style>
  :root {
    --board: #a3a3a3;
    --brand-orange: #ef5527;
    --brand-orange-deep: #c9421b;
    --brand-amber: #f08a32;
    --brand-lime: #d4df5a;
    --paper: #ffffff;
    --ink-label: #ffffff;
  }
  html, body {
    margin: 0;
    width: 1178px;
    height: 1200px;
    overflow: hidden;
    background: var(--board);
  }
  .presentation-board {
    display: block;
    width: 1178px;
    height: 1200px;
  }
  .side-label {
    font-family: "Alegreya Sans", sans-serif;
    font-weight: 700;
    font-size: 30px;
    fill: var(--ink-label);
  }
  .brand-name {
    font-family: "Alegreya Sans", sans-serif;
    font-weight: 400;
    font-size: 58px;
    fill: var(--brand-orange);
    letter-spacing: 3px;
  }
  .contact-text {
    font-family: "Alegreya Sans", sans-serif;
    font-style: italic;
    font-size: 19px;
    fill: var(--paper);
  }
</style>
</head>
<body>
<svg class="presentation-board" viewBox="0 0 900 900" preserveAspectRatio="none" xmlns="http://www.w3.org/2000/svg">
  <defs>
    <clipPath id="front-card-area"><rect x="193" y="76" width="515" height="309"/></clipPath>
    <clipPath id="back-card-area"><rect x="193" y="505" width="515" height="308"/></clipPath>
    <linearGradient id="band-shade" x1="0" y1="0" x2="0" y2="1">
      <stop offset="0" stop-color="#000" stop-opacity="0.18"/>
      <stop offset="1" stop-color="#000" stop-opacity="0"/>
    </linearGradient>
  </defs>

  <!-- Front of card -->
  <g class="card-front" clip-path="url(#front-card-area)">
    <rect x="193" y="76" width="515" height="309" fill="var(--brand-orange)"/>
    <path d="M193 386 C430 380 706 300 696 180 C692 130 671 95 646 76 L193 76 Z" fill="var(--brand-amber)"/>
    <path d="M193 386 C425 380 698 300 688 180 C684 130 663 95 638 76 L193 76 Z" fill="var(--brand-lime)"/>
    <path d="M193 386 C415 378 684 298 676 182 C672 132 652 96 625 76 L193 76 Z" fill="var(--paper)"/>
    <text class="brand-name" x="450" y="250" text-anchor="middle">KGDB</text>
  </g>

  <text class="side-label" x="450" y="449" text-anchor="middle">FRONT</text>

  <!-- Back of card -->
  <g class="card-back" clip-path="url(#back-card-area)">
    <rect x="193" y="505" width="515" height="308" fill="var(--brand-orange)"/>
    <polygon points="193,815 708,520 708,600 193,870" fill="url(#band-shade)" opacity="0.6"/>
    <polygon points="540,505 720,813 640,813 470,560" fill="var(--brand-orange-deep)" opacity="0.35"/>
    <line x1="518" y1="500" x2="702" y2="818" stroke="var(--paper)" stroke-width="22"/>
    <line x1="518" y1="500" x2="702" y2="818" stroke="var(--brand-lime)" stroke-width="14"/>
    <line x1="185" y1="806" x2="716" y2="506" stroke="var(--paper)" stroke-width="24"/>
    <line x1="185" y1="806" x2="716" y2="506" stroke="var(--brand-lime)" stroke-width="15"/>

    <g class="contact-person" transform="translate(514 552) rotate(-30)">
      <text class="contact-text" x="0" y="0" text-anchor="end">Marcus Delwyn, Store Manager</text>
      <text class="contact-text" x="4" y="24" text-anchor="end">(210) 555-0143</text>
    </g>
    <g class="contact-address" transform="translate(566 640) rotate(-30)">
      <text class="contact-text" x="0" y="0" text-anchor="end">Bright Circuit Mending Depot LLC</text>
      <text class="contact-text" x="4" y="24" text-anchor="end">3478 S Ridge Trail 2210 E</text>
      <text class="contact-text" x="6" y="48" text-anchor="end">Suite 417</text>
      <text class="contact-text" x="8" y="90" text-anchor="end">San Antonio, TX 78341</text>
    </g>
  </g>
</svg>
</body>
</html>
```